Training Manual

We need a black/white InDesign template created for our training manual. We're looking to slightly modernize the design and make it as visually appealing as possible while also remaining highly-readable and not tiring to look at at for long periods of time.
A sample chapter from our current manual is attached. - The manual overall consists of 260 pages, there are a few diagrams but the manual consists primarily of text.
Training

```html
<!DOCTYPE html>
<html lang="en">
<head>
<meta charset="utf-8">
<title>05 The Devotional Life</title>
<link rel="stylesheet" href="https://fonts.googleapis.com/css2?family=Inter+Tight:ital,wght@0,300;0,400;0,500;0,700;1,400&display=swap">
<style>
:root{
  --paper:#ffffff;
  --ink:#111111;
  --ink-soft:#2a2a2a;
  --mark:#9a9a9a;
  --rule:#e6e6e6;
  --photo:#d2d1d2;
}
*{margin:0;padding:0;box-sizing:border-box;}
html,body{width:1200px;height:1000px;overflow:hidden;background:var(--paper);}
body{position:relative;font-family:"Inter Tight",Helvetica,Arial,sans-serif;color:var(--ink);}
.crop-marks{position:absolute;left:0;top:0;}
.running-head{position:absolute;left:52px;top:123px;font-size:7px;font-style:italic;}
.chapter-title{position:absolute;left:54px;top:280px;font-size:36px;letter-spacing:-0.6px;line-height:1;}
.chapter-title .num{font-weight:300;}
.chapter-title .name{font-weight:700;}
.column{position:absolute;width:246px;font-size:7.4px;line-height:9.1px;color:var(--ink-soft);}
.column p{margin-bottom:10px;font-weight:500;}
.column .quote{font-style:italic;font-weight:400;}
.section-head{font-size:9.5px;font-weight:700;color:var(--ink);margin-bottom:14px;}
.section-head.large{font-size:10.5px;font-weight:400;margin-top:18px;margin-bottom:12px;}
.section-head.large b{font-weight:700;}
.sub-head{font-size:8px;font-weight:500;color:var(--ink);margin-bottom:11px;}
.sub-head.caps{font-size:9.5px;font-weight:700;margin-top:14px;}
.photo-area{position:absolute;left:633px;top:130px;width:514px;height:348px;background:var(--photo);}
.folio{position:absolute;right:56px;top:871px;font-size:7px;}
.folio .manual{font-style:italic;margin-right:14px;}
.folio .page{font-weight:700;}
</style>
</head>
<body>

<svg class="crop-marks" width="1200" height="1000" aria-hidden="true">
  <g stroke="var(--mark)" stroke-width="0.6">
    <line x1="0" y1="88" x2="18" y2="88"/><line x1="1182" y1="88" x2="1200" y2="88"/>
    <line x1="0" y1="908" x2="18" y2="908"/><line x1="1182" y1="908" x2="1200" y2="908"/>
    <line x1="30" y1="68" x2="30" y2="80"/><line x1="572" y1="68" x2="572" y2="80"/>
    <line x1="628" y1="68" x2="628" y2="80"/><line x1="1170" y1="68" x2="1170" y2="80"/>
    <line x1="30" y1="918" x2="30" y2="930"/><line x1="572" y1="918" x2="572" y2="930"/>
    <line x1="628" y1="918" x2="628" y2="930"/><line x1="1170" y1="918" x2="1170" y2="930"/>
  </g>
  <g stroke="var(--rule)" stroke-width="0.6">
    <line x1="20" y1="88" x2="1180" y2="88"/>
    <line x1="20" y1="908" x2="1180" y2="908"/>
    <line x1="600" y1="88" x2="600" y2="908"/>
  </g>
</svg>

<div class="running-head">05 The Devotional Life</div>
<h1 class="chapter-title"><span class="num">05 </span><span class="name">The Devotional Life</span></h1>

<section class="column" style="left:52px;top:379px;">
  <h2 class="section-head">I. “This Is Eternal Life”</h2>
  <p>A. In John 17:3 Jesus describes eternal life as knowing the only true God and the One He has sent. This kind of “knowing” goes far beyond a passing acquaintance. It points to a deep and lasting bond; a personal, experiential [grounded in lived experience] relationship with the Father and with the Son.</p>
  <p class="quote">Personal faith among believers has grown thin. There is plenty of outward form, plenty of activity, plenty of talk about religion… What we truly need is to know God and the reach of His love, as shown in Christ, through real experience. – Letters to the Church, vol. 5, p. 743.</p>
  <p>B. Every meaningful relationship needs investment; it takes time and care to grow. It also depends on healthy communication, and that communication has to run both ways. We do not only speak to God, we also receive what He says to us. We are not only to talk; we must learn to listen as well. The devotional life – speaking to God in prayer and hearing Him through reflection and the study of His word – is how a saving relationship with God is built. We address God in prayer, and He answers us through His Word.</p>
  <p class="quote">Go to your quiet place with the Scriptures open before you, and there spend time with God, ready to hear what the Spirit is saying to you. Let your heart grow humble and willing to learn, made gentle and yielding by the Spirit. If you discover that views you once held are not supported by Scripture, it is to your lasting good to learn it as early as you can; for when God speaks through His word, our fixed opinions must give way, and our thinking must be brought into line with what He has said. – Weekly Messenger, Dec. 24 1895.</p>
  <p>C. The enemy understands this clearly, and does everything within his reach to disrupt the devotional habits of God’s people.</p>
  <p class="quote">A pressure unlike anything seen before is gripping the world. In leisure, in earning, in the race for influence, in the simple effort to survive, a powerful current sweeps up body, mind and spirit. In the middle of this frantic rush, God is calling. He invites us to step aside and spend time with Him. “Be still, and know that I am God.” Psalm 46:10. Many, even during their times of worship, miss the blessing of genuine fellowship with God. They move too quickly. With rushed</p>
</section>

<section class="column" style="left:315px;top:405px;">
  <p class="quote">steps they pass through the circle of His presence, lingering perhaps for a moment in that holy place, but not staying to be taught. They have no time to wait with the Teacher. Still carrying their loads, they go back to their tasks. – Lessons for Life, p. 260.</p>
  <p class="quote">The adversary knows that anyone he can draw away from prayer and from searching the Scriptures will fall before his assaults. So he devises every possible distraction to fill the mind… – The Long Struggle, p. 519.</p>
  <p>D. No amount of prayer or Bible study will benefit someone who is unwilling to bring the truth into everyday living. Scripture describes the person who hears but does not act as one who is self-deceived (Ja. 1:22; Mt. 7:26-7). Gaining knowledge is only one step. Jesus taught that whoever truly wants to know the truth must be ready to live it (Jn. 7:17; 12:35). Personal application means acting on what we learn and passing it on to others.</p>
  <p class="quote">Truth means little to those who never live it out. Truth becomes real to you only as you practice it day by day… – Collected Papers, p. 1744.</p>
  <p class="quote">Whoever does nothing except pray will soon stop praying, or the prayers will turn into empty habit. When people withdraw from others, away from the field of service and shared burdens; when they stop working wholeheartedly for the Master, who gave Himself for them, they lose the very substance of prayer and the motive for devotion. – The Path of Grace, p. 101.</p>
  <h2 class="section-head large"><b>II. Personal Prayer</b> – The Key to Spiritual Power</h2>
  <p>A. Prayer is the secret to Spiritual power.</p>
  <p>1. Prayer is vital to spiritual life and to every spiritual task. Just as the body needs air to keep living, the soul needs prayer to keep its life. Prayer is the breathing of the soul. – Field Workers, p. 254. Darkness closes in around those who stop praying. – Ibid., p. 94.</p>
</section>

<div class="photo-area" role="img" aria-label="Chapter photograph: a person in quiet prayer or Bible study"></div>

<section class="column" style="left:633px;top:497px;">
  <p>2. Without prayer, our faith shrinks into an empty outward shell, much like the “dry bones” that heard the word spoken over them, yet had not received the breath of life (Ezek. 37:7-8). This was the state of the church in Christ’s time; they studied the Scriptures to gather facts rather than to know God personally. Jesus noted their careful reading, but added “You are not willing to come to Me that you may have life” (Jn. 5:39-40).</p>
  <p class="quote">[Prayer] is the source of spiritual strength. No other practice can take its place while the soul stays healthy. Prayer connects the heart directly with the Fountain of life, and builds up the strength and endurance of our faith. Let prayer lapse, or pray only in fits and starts, here and there, whenever it suits, and your grip on God loosens. The powers of the spirit fade, and the life of faith loses its health and energy. – Field Workers, p. 254.</p>
  <p>3. This is why we are urged to “pray without ceasing” (1 Thess. 5:17). It does not mean long, drawn-out, formal prayers, but living in a posture of open conversation with God, a bit like staying on a call with a friend and never hanging up.</p>
  <p class="quote">We are told, “Pray without ceasing;” that is, keep the thoughts turned toward God, the source of all strength and ability. - Letters to Pastors, p. 510.</p>
  <p class="quote">Constant prayer is the unbroken bond of the soul with God… - The Path of Grace, p. 97.</p>
  <p class="quote">Pray in private, and as you carry out your daily work let your heart turn often toward God. This is how Enoch walked with God. – Ibid., pp. 98-99.</p>
</section>

<section class="column" style="left:895px;top:497px;">
  <p class="quote">Build the habit of speaking with the Saviour when you are alone, while you are walking, and while you are occupied with your daily work. Let the heart keep rising in quiet requests for help, for light, for strength, for understanding. Let every breath become a prayer. – On Prayer, p. 179.</p>
  <p class="quote">Daily prayer is as necessary to growth in grace, and even to spiritual life itself, as daily bread is to physical health. We should train ourselves to lift our thoughts to God often. When the mind drifts, we must gently return it; with steady effort, the habit will at last feel natural. We are never safe apart from Christ, not even for a moment. His presence can go with us every step, but only as we follow the terms He has set out for us. – Daily Grace, p. 289.</p>
  <h3 class="sub-head caps">B. HOW TO PRAY</h3>
  <h4 class="sub-head">1. Determine a Time and Place for Prayer</h4>
  <p>a. Every devotional practice takes time, and we should keep a set time for personal, “secret” prayer with God. Daniel prayed three times each day. Jesus, our model in all things, spent long hours in prayer (Lk. 6:12). Scripture records that “In the morning, having risen a long while before daylight, He went out and departed to a solitary place; and there He prayed” (Mk. 1:35). Both kept a regular time and place for “secret prayer”.</p>
  <p class="quote">We should pray together as a family, and most of all we must not neglect private prayer, for it is the life of the soul. The soul cannot thrive while prayer is left aside. Family or group prayer by itself is not enough. – The Path of Grace, p. 98.</p>
</section>

<footer class="folio"><span class="manual">Covenant Institute Training Manual</span><span class="page">31</span></footer>

</body>
</html>
```